Real Estate For Sale Signage

I'm an independent agent in Lismore NSW Australia with high standards and looking for a catching 'For Sale'sign board.
I like classy, elegant, stylish and simple best.
My colours are red, white and black.
I don't have a logo or other font designs I need to stick to. I like the concept of a house or real estate design.
Before I created this project I played around on publisher and created the PDF attached. I'm not sold on it, but I don't mind the way the name has been layed out. Originally I had a white background with black & red font.
Fancy fonts for my name would be nice, but must not be busy.
Updates

Just wanted to advise that I have updated my brief and used the tools available to help get my ideas through.

Thank you for your work and time.

Kind regards
Marella

Industry/Entity Type

Real Estate

Requirements
Must have
• For Sale
Marella Quint Real Estate (must stand out)
0400 517 382 (must stand out)
17 Tallowood Street North Lismore
www.marellaquintrealestate.com.au

```html
<!DOCTYPE html>
<html lang="en">
<head>
<meta charset="utf-8">
<title>Marella Quint Real Estate – For Sale Sign</title>
<link rel="stylesheet" href="https://fonts.googleapis.com/css2?family=Open+Sans:wght@700&family=PT+Sans:ital,wght@1,700&family=Roboto:ital,wght@1,900&family=Uncial+Antiqua&display=swap">
<style>
  :root {
    --page: #ffffff;
    --roof-blue: #4658c2;
    --wall-blue: #344696;
    --door-white: #ffffff;
    --sign-white: #ffffff;
    --brand-orange: #e0652b;
    --brand-red: #d93a26;
    --hand-red: #ff1a00;
    --digit-red: #e8402a;
    --digit-orange: #f0a060;
    --digit-edge: #c9cbd2;
  }
  html, body {
    margin: 0;
    padding: 0;
    width: 1140px;
    height: 1200px;
    overflow: hidden;
    background: var(--page);
  }
  .sign {
    display: block;
    width: 1140px;
    height: 1200px;
  }
  .roof { fill: var(--roof-blue); }
  .wall { fill: var(--wall-blue); }
  .door { fill: var(--door-white); }
  .brand-mark { fill: var(--brand-red); }
  .hand-art { fill: var(--hand-red); }

  .for-sale {
    font-family: "Open Sans", "Myriad Pro", sans-serif;
    font-weight: 700;
    font-size: 104px;
    letter-spacing: -2px;
    fill: var(--sign-white);
  }
  .for-sale--diagonal {
    font-size: 98px;
  }
  .brand-name {
    font-family: "Uncial Antiqua", serif;
    font-size: 66px;
    fill: var(--brand-orange);
  }
  .phone-label {
    font-family: "Uncial Antiqua", serif;
    font-size: 34px;
    fill: var(--sign-white);
  }
  .phone-number {
    font-family: "Roboto", "Arial Black", sans-serif;
    font-style: italic;
    font-weight: 900;
    font-size: 70px;
    stroke: var(--digit-edge);
    stroke-width: 4px;
    paint-order: stroke;
  }
  .contact-line {
    font-family: "PT Sans", sans-serif;
    font-style: italic;
    font-weight: 700;
    font-size: 29px;
    fill: var(--sign-white);
  }
</style>
</head>
<body>
<svg class="sign" viewBox="0 0 1140 1200" xmlns="http://www.w3.org/2000/svg">
  <defs>
    <linearGradient id="digitFill" x1="0" y1="0" x2="1" y2="0">
      <stop offset="0" stop-color="#9a1a14"/>
      <stop offset="0.25" stop-color="var(--digit-red)"/>
      <stop offset="0.5" stop-color="var(--digit-orange)"/>
      <stop offset="0.8" stop-color="var(--digit-red)"/>
      <stop offset="1" stop-color="#b8241a"/>
    </linearGradient>
    <filter id="digitShadow" x="-10%" y="-30%" width="130%" height="180%">
      <feDropShadow dx="6" dy="12" stdDeviation="4" flood-color="#000" flood-opacity="0.9"/>
    </filter>
  </defs>

  <!-- Roof -->
  <polygon class="roof" points="572,94 1064,383 80,383"/>
  <text class="for-sale for-sale--diagonal" transform="translate(264,378) rotate(-30.4)">For Sale</text>
  <text class="for-sale" x="503" y="345">For Sale</text>

  <!-- House body -->
  <rect class="wall" x="111" y="414" width="892" height="671"/>
  <rect class="door" x="683" y="619" width="148" height="466"/>

  <!-- Agency name -->
  <rect class="brand-mark" x="135" y="453" width="226" height="226"/>
  <text class="brand-name" x="392" y="513" textLength="590" lengthAdjust="spacingAndGlyphs">Marella Quint</text>
  <text class="brand-name" x="401" y="606" textLength="456" lengthAdjust="spacingAndGlyphs">Real Estate</text>

  <!-- Contact -->
  <text class="phone-label" x="176" y="733">Phone</text>
  <text class="phone-number" x="174" y="818" textLength="505" lengthAdjust="spacingAndGlyphs" fill="url(#digitFill)" filter="url(#digitShadow)">0400 517 382</text>
  <text class="contact-line" x="176" y="883">17 Tallowood Street North Lismore</text>
  <text class="contact-line" x="176" y="921">www.marellaquintrealestate.com.au</text>

  <!-- Welcoming hand at the door -->
  <g role="img" aria-label="Red hand reaching out from the doorway in welcome">
    <rect class="hand-art" x="760" y="866" width="202" height="178" rx="40"/>
  </g>
</svg>
</body>
</html>
```